Torvane Travel Business Card Design

We need a new business card design for our travel agency business - Torvane Travel. We design packages to some of the most popular travel destinations in the world for groups, individuals and also tailor-make personalised packages. Our logo attached must be used. On the back of the card we would like a list of all websites under our Torvane brand to be posted. We would like clean, modern, simple design.

Industry/Entity Type

Travel Agent

Contact Information for Business Card

Owen Pridmore
National Sales Manager
Reservations: 1300 742 689
Tel: 61 28473 5096
Fax: 61 2847 3971
Email: owen@torvanetravel.com.au
Web: www.torvanetravel.com.au

Address: Level 1, 417 Harwick Street
Sydney NSW 2000 Australia

Requirements
Must have
• On the back of the card we want all websites listed under our Torvane brand.
• Torvane Travel Group - Wholesale Specialists
• www.qpjourneys.com.au - New Caledonia
• www.bravelmijourneys.com.au - Tahiti
• www.sorvenbreakhub.com.au - China
Nice to have
• Modern, clean lined, simple and fresh
Should not have
• Look dull

```html
<!DOCTYPE html>
<html lang="en">
<head>
<meta charset="utf-8">
<title>Torvane Travel Business Card</title>
<link href="https://fonts.googleapis.com/css2?family=Open+Sans:wght@400;600;700&display=swap" rel="stylesheet">
<style>
  :root {
    --blue: #2e2f8f;
    --red: #e11d2e;
    --ink: #3a3b7a;
    --rule: #b9bacb;
    --card: #ffffff;
    --stage: #e9e6e1;
  }
  * { margin: 0; padding: 0; box-sizing: border-box; }
  html, body { width: 1200px; height: 973px; overflow: hidden; }
  body {
    background: var(--stage);
    font-family: "Open Sans", Arial, sans-serif;
    position: relative;
  }
  .card {
    position: absolute;
    width: 540px;
    height: 330px;
    background: var(--card);
    border-radius: 18px;
    overflow: hidden;
    box-shadow: 0 10px 28px rgba(0,0,0,.18);
  }
  .card--front { left: 50px; top: 130px; }
  .card--back { left: 610px; top: 500px; }

  .brand-name {
    font-weight: 600;
    color: var(--blue);
    letter-spacing: -0.5px;
    white-space: nowrap;
  }

  /* front */
  .front-brand { position: absolute; right: 40px; top: 40px; text-align: right; }
  .front-brand .brand-name { font-size: 36px; line-height: 1; }
  .front-rule { position: absolute; left: 140px; right: 30px; top: 96px; height: 1px; background: var(--rule); }
  .job-title { position: absolute; right: 30px; top: 102px; font-size: 12px; color: var(--red); }
  .person-name { position: absolute; left: 34px; top: 150px; font-size: 17px; font-weight: 700; color: var(--blue); letter-spacing: .5px; }
  .person-name::after { content: ""; display: block; width: 150px; height: 3px; background: var(--red); margin-top: 4px; }
  .contact { position: absolute; font-size: 13px; color: var(--ink); line-height: 1.45; }
  .contact .label { color: var(--red); font-size: 11px; margin-right: 4px; }
  .contact--phones { left: 34px; top: 196px; }
  .contact--online { left: 200px; top: 196px; }
  .contact--address { left: 34px; top: 244px; }
  .front-bands { position: absolute; left: 0; bottom: 0; width: 540px; height: 110px; }
  .reservations { position: absolute; right: 24px; bottom: 26px; color: #fff; text-align: left; }
  .reservations .label { font-size: 12px; display: block; }
  .reservations .number { font-size: 19px; }

  /* back */
  .back-brand { position: absolute; left: 0; right: 0; top: 70px; text-align: center; }
  .back-brand .brand-name { font-size: 46px; line-height: 1; }
  .back-rule { position: absolute; left: 80px; right: 80px; top: 150px; height: 1px; background: var(--rule); }
  .group-line { position: absolute; left: 0; right: 0; top: 160px; text-align: center; font-size: 15px; color: var(--ink); }
  .sites { position: absolute; left: 22px; right: 22px; top: 222px; display: flex; justify-content: space-between; list-style: none; }
  .site { font-size: 11.5px; color: var(--ink); }
  .site .region { display: block; color: var(--red); font-size: 9.5px; text-transform: uppercase; margin-bottom: 3px; }
</style>
</head>
<body>

<section class="card card--front" aria-label="Business card front">
  <div class="front-brand">
    <div class="brand-name">Torvane Travel</div>
  </div>
  <div class="front-rule"></div>
  <div class="job-title">National Sales Manager</div>

  <div class="person-name">OWEN PRIDMORE</div>

  <div class="contact contact--phones">
    <div><span class="label">Tel.</span>61 28473 5096</div>
    <div><span class="label">Fax.</span>61 2847 3971</div>
  </div>
  <div class="contact contact--online">
    <div><span class="label">E-mail.</span>owen@torvanetravel.com.au</div>
    <div><span class="label">Website.</span>www.torvanetravel.com.au</div>
  </div>
  <div class="contact contact--address">
    <div>Level 1, 417 Harwick Street</div>
    <div>Sydney NSW 2000 Australia</div>
  </div>

  <svg class="front-bands" viewBox="0 0 540 110" aria-hidden="true">
    <rect x="0" y="96" width="540" height="14" fill="var(--blue)"/>
    <path d="M360 110 C 368 80, 345 52, 380 34 C 420 16, 480 10, 540 6 L540 110 Z" fill="var(--red)"/>
  </svg>
  <div class="reservations">
    <span class="label">Reservations</span>
    <span class="number">1300 742 689</span>
  </div>
</section>

<section class="card card--back" aria-label="Business card back">
  <div class="back-brand">
    <div class="brand-name">Torvane Travel</div>
  </div>
  <div class="back-rule"></div>
  <div class="group-line">Torvane Travel Group - Wholesale Specialists</div>
  <ul class="sites">
    <li class="site"><span class="region">New Caledonia</span>www.qpjourneys.com.au</li>
    <li class="site"><span class="region">Tahiti</span>www.bravelmijourneys.com.au</li>
    <li class="site"><span class="region">China</span>www.sorvenbreakhub.com.au</li>
  </ul>
</section>

</body>
</html>
```